Logo design and Businesscard and letterhead for Technology Company

We need logo design for a new company based in Atlanta called "Plovenix". We provide information about technology Product and service provider companies, information about their Products and services. Our initial focus is to List various companies and their products, various consulting companies and their services. We want to convey the message that this will be one stop shop to find out all the information to make smart technology decisions

I am looking for Logo, Business Card and Letterhead.

Target Market(s)

Companies that have IT department, IT users such as Developers, Managers, C level, Technology Product companies , Consulting companies and service providers.

Industry/Entity Type

It Company

Requirements
Must have
• Looking for some Unique design idea.
Nice to have
• I want something that connects information across technologies between technology buyers and sellers.
Should not have
• No puzzle design.

```html
<!DOCTYPE html>
<html lang="en">
<head>
<meta charset="utf-8">
<title>Plovenix – Stationery</title>
<link href="https://fonts.googleapis.com/css2?family=Michroma&display=swap" rel="stylesheet">
<style>
  :root {
    --orange: #ff5a00;
    --grey-text: #5f5e5c;
    --band-grey: #dedddc;
    --paper: #ffffff;
    --page: #ffffff;
  }
  * { margin: 0; padding: 0; box-sizing: border-box; }
  html, body { width: 818px; height: 1200px; overflow: hidden; background: var(--page); }
  body { position: relative; font-family: "Michroma", sans-serif; }

  .wordmark {
    position: absolute;
    color: var(--orange);
    font-family: "Michroma", sans-serif;
    font-weight: 400;
    white-space: nowrap;
    line-height: 1;
    letter-spacing: -0.02em;
  }
  .wordmark--hero { left: 36px; top: 18px; font-size: 144px; }

  .letterhead {
    position: absolute;
    left: 27px; top: 201px;
    width: 765px; height: 976px;
    background: var(--paper);
    box-shadow: 0 0 22px rgba(0,0,0,0.28);
  }
  .letterhead > .wordmark { left: 40px; top: 32px; font-size: 56px; }

  .contact {
    position: absolute;
    color: var(--grey-text);
    font-style: normal;
    font-size: 10.5px;
    line-height: 11.4px;
    letter-spacing: 0.2em;
    font-variant: small-caps;
    white-space: nowrap;
  }
  .contact .name { color: var(--orange); font-size: 12px; line-height: 13px; }

  .rule { position: absolute; }
  .rule .band { background: var(--band-grey); }
  .rule .accent { background: var(--orange); }

  .letterhead .contact--header { left: 180px; top: 104px; }
  .rule--header { left: 0; top: 152px; width: 378px; }
  .rule--header .band { height: 18px; }
  .rule--header .accent { height: 10px; }

  .letterhead .contact--sign { left: 403px; top: 790px; font-size: 9.8px; }
  .rule--sign { left: 403px; top: 851px; width: 362px; }
  .rule--sign .band { height: 19px; }
  .rule--sign .accent { height: 9px; }

  .business-card {
    position: absolute;
    left: 405px; top: 281px;
    width: 324px; height: 184px;
    background: var(--paper);
    border-radius: 6px;
    box-shadow: 0 0 6px rgba(0,0,0,0.3);
    overflow: hidden;
  }
  .business-card .wordmark { left: 18px; top: 16px; font-size: 27px; }
  .rule--card-top { left: 0; top: 52px; width: 195px; }
  .rule--card-top .band { height: 8px; }
  .rule--card-top .accent { height: 4px; }
  .business-card .contact--card { left: 153px; top: 93px; font-size: 9.6px; line-height: 10.6px; letter-spacing: 0.18em; }
  .rule--card-bottom { left: 152px; top: 152px; width: 172px; }
  .rule--card-bottom .band { height: 9px; }
  .rule--card-bottom .accent { height: 4px; }
</style>
</head>
<body>
  <div class="wordmark wordmark--hero">Plovenix</div>

  <section class="letterhead">
    <div class="wordmark">Plovenix</div>
    <address class="contact contact--header">
      418 Plovenix Rd.<br>City, State<br>P (555) 014-2270<br>F (555) 014-2271
    </address>
    <div class="rule rule--header"><div class="band"></div><div class="accent"></div></div>

    <address class="contact contact--sign">
      <span class="name">Jane Rowe</span><br>418 Plovenix Rd.<br>City, State<br>P (555) 014-2270<br>F (555) 014-2271
    </address>
    <div class="rule rule--sign"><div class="band"></div><div class="accent"></div></div>

    <div class="business-card">
      <div class="wordmark">Plovenix</div>
      <div class="rule rule--card-top"><div class="band"></div><div class="accent"></div></div>
      <address class="contact contact--card">
        <span class="name">Jane Rowe</span><br>418 Plovenix Rd.<br>City, State<br>P (555) 014-2270<br>F (555) 014-2271
      </address>
      <div class="rule rule--card-bottom"><div class="band"></div><div class="accent"></div></div>
    </div>
  </section>
</body>
</html>
```